"We are still here" postcard

An employee has left the company and is soliciting clients leaving them to believe I have shut down. Need to convey graphic message that we are still operating and continue the great service they have always had. We prepare income taxes. The office has a train theme within and is located on historic Corwin Street. Some ideas might be yin/yang light/dark up/down steam engine/caboose

Our colors are
98a9b7
3aa9ae
3c4c80
ab3c51

```html
<!DOCTYPE html>
<html lang="en">
<head>
<meta charset="utf-8">
<title>We Are Still Here – Postcard</title>
<link rel="stylesheet" href="https://fonts.googleapis.com/css2?family=Roboto+Condensed:wght@700;800&family=Poppins:wght@400;500;600;700&display=swap">
<style>
  :root {
    --teal: #2fa7ad;
    --grey-band: #9aa7b4;
    --ink: #2f3236;
    --paper: #f7f7f7;
    --white: #ffffff;
    --backdrop: #e6d6d3;
    --rule: #555a60;
    --photo-light: #4f7f8a;
    --photo-mid: #2b3a42;
    --photo-dark: #161f26;
  }
  * { box-sizing: border-box; margin: 0; padding: 0; }
  html, body {
    width: 1200px; height: 1198px; overflow: hidden;
    background: var(--backdrop);
  }
  .canvas { position: relative; width: 1200px; height: 1198px; }
  .card {
    position: absolute; overflow: hidden; background: var(--paper);
    font-family: "Poppins", sans-serif;
  }
  .card svg.art { position: absolute; inset: 0; width: 100%; height: 100%; }
  .front { left: 292px; top: 100px; width: 704px; height: 468px; }
  .back  { left: 294px; top: 613px; width: 702px; height: 469px; }

  .headline {
    position: absolute;
    font-family: "Roboto Condensed", sans-serif;
    font-weight: 800; color: var(--white); line-height: 1;
    letter-spacing: 0;
  }
  .headline .line-1 { display: block; }
  .headline .line-2 { display: block; }
  .headline .accent { color: var(--teal); }
  .headline .rule { display: block; height: 3px; background: var(--white); }

  .front .headline { right: 38px; top: 52px; text-align: right; }
  .front .line-1 { font-size: 104px; }
  .front .line-2 { font-size: 72px; margin-top: 18px; }
  .front .rule { width: 298px; margin-top: 22px; margin-left: auto; }

  .back .headline { left: 54px; top: 40px; }
  .back .line-1 { font-size: 82px; }
  .back .line-2 { font-size: 56px; margin-top: 14px; }
  .back .rule { width: 246px; margin-top: 16px; }

  .brand-name {
    position: absolute; left: 70px; top: 232px; width: 196px;
    text-align: center;
    font-family: "Roboto Condensed", sans-serif; font-weight: 800;
    font-size: 58px; line-height: 1.08; color: var(--teal);
  }

  .contact {
    position: absolute; display: flex; align-items: center; gap: 8px;
    font-size: 13px; color: var(--ink);
  }
  .contact svg { width: 16px; height: 16px; }
  .front .contact-email { left: 64px; top: 437px; }
  .front .contact-web { left: 490px; top: 437px; }
  .back .contact { color: var(--white); font-size: 12px; gap: 6px; }
  .back .contact svg { width: 13px; height: 13px; }
  .back .contact-email { left: 18px; top: 441px; }
  .back .contact-web { left: 180px; top: 441px; }

  .stamp-box {
    position: absolute; left: 552px; top: 47px; width: 98px; height: 93px;
    border: 1.5px solid var(--ink);
  }
  .address-lines { position: absolute; left: 440px; top: 198px; width: 210px; }
  .address-lines span {
    display: block; height: 1px; background: var(--rule); margin-bottom: 32px;
  }

  .call-block { position: absolute; left: 458px; top: 398px; display: flex; gap: 10px; }
  .call-block svg { width: 32px; height: 30px; margin-top: 6px; }
  .call-label { font-size: 15px; color: var(--teal); line-height: 1.2; }
  .call-number { font-size: 24px; font-weight: 700; color: var(--ink); line-height: 1.1; letter-spacing: -0.3px; font-family: "Roboto Condensed", sans-serif; }
</style>
</head>
<body>
<main class="canvas">

  <!-- Front side -->
  <section class="card front">
    <svg class="art" viewBox="0 0 704 468" preserveAspectRatio="none">
      <defs>
        <linearGradient id="frontPhoto" x1="0" y1="0" x2="1" y2="0.4">
          <stop offset="0" stop-color="var(--photo-light)"/>
          <stop offset="0.45" stop-color="var(--photo-mid)"/>
          <stop offset="1" stop-color="var(--photo-dark)"/>
        </linearGradient>
      </defs>
      <rect role="img" aria-label="Photo of a vintage steam locomotive pulling carriages through steam" width="704" height="330" fill="url(#frontPhoto)"/>
      <path d="M0,282 C150,234 300,344 480,344 C580,344 650,312 704,292 L704,468 L0,468 Z" fill="var(--paper)"/>
      <path d="M0,268 C150,220 300,330 480,330 C580,330 650,300 704,280" fill="none" stroke="var(--teal)" stroke-width="18"/>
      <path d="M0,292 C150,246 300,356 480,356 C580,356 650,326 704,306" fill="none" stroke="var(--grey-band)" stroke-width="10"/>
      <path d="M40,322 C180,280 320,380 490,378 C590,376 650,348 704,330" fill="none" stroke="var(--teal)" stroke-width="4"/>
      <circle cx="168" cy="311" r="102" fill="var(--teal)" opacity="0.25"/>
      <circle cx="168" cy="311" r="96" fill="var(--white)"/>
      <circle cx="281" cy="338" r="25" fill="var(--teal)"/>
    </svg>

    <h1 class="headline">
      <span class="line-1">WE ARE</span>
      <span class="line-2"><span class="accent">STILL</span> HERE</span>
      <span class="rule"></span>
    </h1>

    <div class="brand-name">YOUR LOGO</div>

    <div class="contact contact-email">
      <svg viewBox="0 0 16 16"><rect x="1" y="3" width="14" height="10" fill="none" stroke="var(--teal)" stroke-width="1.6"/><path d="M1,3 L8,9 L15,3" fill="none" stroke="var(--teal)" stroke-width="1.6"/></svg>
      <span>info@corwintaxhouse.com</span>
    </div>
    <div class="contact contact-web">
      <svg viewBox="0 0 16 16"><circle cx="8" cy="8" r="6.5" fill="none" stroke="var(--teal)" stroke-width="1.6"/><ellipse cx="8" cy="8" rx="2.8" ry="6.5" fill="none" stroke="var(--teal)" stroke-width="1.3"/><path d="M1.5,8 H14.5" stroke="var(--teal)" stroke-width="1.3"/></svg>
      <span>www.corwintaxhouse.com</span>
    </div>
  </section>

  <!-- Back side -->
  <section class="card back">
    <svg class="art" viewBox="0 0 702 469" preserveAspectRatio="none">
      <defs>
        <linearGradient id="backPhoto" x1="0" y1="0" x2="0.3" y2="1">
          <stop offset="0" stop-color="#2e4450"/>
          <stop offset="0.55" stop-color="#1d2a35"/>
          <stop offset="1" stop-color="#141b22"/>
        </linearGradient>
      </defs>
      <rect role="img" aria-label="Photo of a steam locomotive seen from the front at dusk" width="400" height="469" fill="url(#backPhoto)"/>
      <path d="M356,0 C440,110 446,200 384,262 C322,324 300,400 356,469 L702,469 L702,0 Z" fill="var(--paper)"/>
      <path d="M344,0 C428,110 434,200 372,262 C310,324 288,400 344,469" fill="none" stroke="var(--teal)" stroke-width="12"/>
      <path d="M330,0 C414,110 420,200 358,262 C296,324 274,400 330,469" fill="none" stroke="var(--grey-band)" stroke-width="8"/>
      <path d="M366,0 C452,112 458,202 396,264 C334,326 314,400 368,469" fill="none" stroke="var(--teal)" stroke-width="3"/>
    </svg>

    <h2 class="headline">
      <span class="line-1">WE ARE</span>
      <span class="line-2"><span class="accent">STILL</span> HERE</span>
      <span class="rule"></span>
    </h2>

    <div class="stamp-box"></div>
    <div class="address-lines"><span></span><span></span><span></span><span></span><span></span><span></span></div>

    <div class="call-block">
      <svg viewBox="0 0 32 30"><path d="M2,3 H20 V15 H9 L4,19 V15 H2 Z" fill="none" stroke="var(--teal)" stroke-width="2" stroke-linejoin="round"/><path d="M23,9 H30 V21 H28 V25 L23,21 H13 V18" fill="none" stroke="var(--teal)" stroke-width="2" stroke-linejoin="round"/><circle cx="7" cy="9" r="1.3" fill="var(--teal)"/><circle cx="11" cy="9" r="1.3" fill="var(--teal)"/><circle cx="15" cy="9" r="1.3" fill="var(--teal)"/></svg>
      <div>
        <p class="call-label">Call us to find more</p>
        <p class="call-number">000 1234 5678</p>
      </div>
    </div>

    <div class="contact contact-email">
      <svg viewBox="0 0 16 16"><rect x="1" y="3" width="14" height="10" fill="none" stroke="var(--white)" stroke-width="1.6"/><path d="M1,3 L8,9 L15,3" fill="none" stroke="var(--white)" stroke-width="1.6"/></svg>
      <span>info@youremail.com</span>
    </div>
    <div class="contact contact-web">
      <svg viewBox="0 0 16 16"><circle cx="8" cy="8" r="6.5" fill="none" stroke="var(--white)" stroke-width="1.6"/><ellipse cx="8" cy="8" rx="2.8" ry="6.5" fill="none" stroke="var(--white)" stroke-width="1.3"/><path d="M1.5,8 H14.5" stroke="var(--white)" stroke-width="1.3"/></svg>
      <span>www.yourwebsite.com</span>
    </div>
  </section>

</main>
</body>
</html>
```